Marou Cay Lodge Christmas wishes 2013

We require postcards designed to mail our to our clients for Christmas. We are a SURF travel company, with a high end market and like to mail our Christmas postcards to all our guests that have stayed with us through the year. Front cover will have images and text (ie Seasons Greeting) and our logo. The back will have space for TO: name & address and postage stamp. Will also have some basic text (ie The Management & Staff at Marou Cay Lodge wish you and your family all the best for the Festive Season and New Year. We look forward to seeing you back at Marou Cay Lodge again soon etc etc). Here is link to main image https://www.filevault-example.com/sh/qwmzrtpx318kle/Zr8pWnQvcB

Target Market(s)

Our clients are mostly mature men (40-70) surfers who purchase luxury surf trips

Industry/Entity Type

Travel

Requirements
Must have
• Ocean Image (front)
Logo x 2 in same colour - Halcyra & Marou Cay Lodge (front)
Text (front)
Back to be white
Space for name & address (back)
Space for postage stamp (back)
Message (back)
Website www.halcyralodges-example.com (back)

```html
<!DOCTYPE html>
<html lang="en">
<head>
<meta charset="utf-8">
<title>Marou Cay Lodge – Season's Greetings Postcards</title>
<link rel="stylesheet" href="https://fonts.googleapis.com/css2?family=Lobster&family=Lobster+Two:ital,wght@1,700&display=swap">
<style>
  :root {
    --page-bg: #ffffff;
    --ink-white: #ffffff;
    --ink-dark: #111111;
    --ink-grey: #5a5a5a;
    --rule-grey: #9a9a9a;
    --frame-grey: #7a7a7a;
    --sea-light: #cfe6f2;
    --sea-mid: #2f86b4;
    --sea-deep: #123f6a;
    --dusk-sky: #d8d3a2;
    --dusk-mid: #6f7a63;
    --dusk-deep: #181b1c;
    --back-green: #93c196;
    --back-teal: #3f6e6f;
    --back-navy: #262a46;
  }
  * { box-sizing: border-box; margin: 0; padding: 0; }
  html, body { width: 1200px; height: 900px; overflow: hidden; background: var(--page-bg); }
  .canvas { position: relative; width: 1200px; height: 900px; }

  .postcard { position: absolute; width: 555px; height: 370px; overflow: hidden; }
  .front-wave { left: 32px; top: 65px; }
  .back-gradient { left: 612px; top: 65px; }
  .front-reef { left: 32px; top: 463px; }
  .back-white { left: 612px; top: 463px; border: 1px solid var(--frame-grey); }

  .photo { position: absolute; inset: 0; }
  .front-wave .photo {
    background:
      radial-gradient(circle at 22% 16%, var(--sea-light) 0, rgba(207,230,242,0.6) 9%, rgba(47,134,180,0) 30%),
      linear-gradient(160deg, var(--sea-mid) 0%, #2a78a6 45%, var(--sea-deep) 100%);
  }
  .front-reef .photo {
    background: linear-gradient(180deg, var(--dusk-sky) 0%, #a9ac85 30%, var(--dusk-mid) 55%, #2c3331 78%, var(--dusk-deep) 100%);
  }

  .brand-lockup {
    position: absolute; left: 0; right: 0; top: 40px;
    text-align: center; color: var(--ink-dark);
    font-family: "Lobster", cursive; line-height: 1.1;
  }
  .brand-parent { font-size: 36px; }
  .brand-lodge { font-size: 30px; margin-top: 14px; }

  .greeting-title {
    position: absolute; left: 0; right: 0; bottom: 18px;
    text-align: center; color: var(--ink-white);
    font-family: "Lobster", cursive; font-size: 66px; line-height: 1;
  }

  .back-gradient {
    background: linear-gradient(90deg, var(--back-green) 0%, var(--back-teal) 40%, var(--back-navy) 100%);
    color: var(--ink-white);
  }
  .back-white { background: var(--page-bg); color: var(--ink-grey); }

  .script { font-family: "Lobster Two", "Lobster", cursive; font-style: italic; font-weight: 700; }

  .message { position: absolute; line-height: 1.08; }
  .back-gradient .message { left: 34px; top: 100px; }
  .back-white .message { left: 325px; top: 125px; }
  .message .sm { font-size: 16px; display: block; }
  .message .md { font-size: 20px; display: block; letter-spacing: 0.3px; }
  .message .lg { font-size: 29px; display: block; }

  .divider { position: absolute; width: 2px; }
  .back-gradient .divider { left: 276px; top: 26px; height: 304px; background: var(--ink-white); }
  .back-white .divider { left: 275px; top: 100px; height: 205px; width: 1px; background: var(--rule-grey); }

  .stamp-box { position: absolute; left: 464px; top: 17px; width: 74px; height: 83px; }
  .back-gradient .stamp-box { border: 1.5px solid var(--ink-white); }
  .back-white .stamp-box { border: 1.5px solid #b5b5b5; }

  .address-block { position: absolute; width: 242px; }
  .back-gradient .address-block { left: 296px; top: 118px; }
  .back-white .address-block { left: 37px; top: 122px; width: 200px; }
  .field-label { font-size: 20px; display: block; height: 28px; }
  .field-line { height: 1px; margin-bottom: 24px; }
  .back-gradient .field-line { background: rgba(255,255,255,0.75); }
  .back-white .field-line { background: var(--rule-grey); margin-bottom: 20px; }
  .field-line.first { margin-top: 18px; }
  .back-white .field-line.first { margin-top: 10px; }

  .farewell {
    position: absolute; left: 0; right: 0; text-align: center; font-size: 14.5px;
  }
  .back-gradient .farewell { top: 344px; }
  .back-white .farewell { top: 332px; }
</style>
</head>
<body>
<main class="canvas">

  <section class="postcard front-wave">
    <div class="photo" role="img" aria-label="Photo of a breaking blue ocean wave with the sun shining through the spray"></div>
    <div class="brand-lockup">
      <div class="brand-parent">Halcyra</div>
      <div class="brand-lodge">Marou Cay Lodge</div>
    </div>
    <h1 class="greeting-title">Seasons greetings!</h1>
  </section>

  <section class="postcard back-gradient">
    <p class="message script">
      <span class="sm">The Management &amp; Staff at</span>
      <span class="md">Marou Cay Lodge</span>
      <span class="sm">wish you and your family</span>
      <span class="md">all the best for the</span>
      <span class="lg">Festive Season</span>
      <span class="lg"><span style="font-size:20px">and</span> New Year</span>
    </p>
    <div class="divider"></div>
    <div class="stamp-box"></div>
    <div class="address-block script">
      <span class="field-label">To:</span>
      <div class="field-line first"></div>
      <div class="field-line"></div>
      <span class="field-label">Adress:</span>
      <div class="field-line first"></div>
      <div class="field-line"></div>
      <div class="field-line"></div>
    </div>
    <p class="farewell script">We look forward to seeing you back at Marou Cay Lodge again!</p>
  </section>

  <section class="postcard front-reef">
    <div class="photo" role="img" aria-label="Photo of a surfer riding a barrelling wave under a cloudy sky with a rainbow over green hills"></div>
    <div class="brand-lockup">
      <div class="brand-parent">Halcyra</div>
      <div class="brand-lodge">Marou Cay Lodge</div>
    </div>
    <h1 class="greeting-title">Seasons greetings!</h1>
  </section>

  <section class="postcard back-white">
    <div class="stamp-box"></div>
    <div class="address-block script">
      <span class="field-label">To:</span>
      <div class="field-line first"></div>
      <div class="field-line"></div>
      <span class="field-label">Adress:</span>
      <div class="field-line first"></div>
      <div class="field-line"></div>
      <div class="field-line"></div>
    </div>
    <div class="divider"></div>
    <p class="message script">
      <span class="sm">The Management &amp; Staff at</span>
      <span class="md">Marou Cay Lodge</span>
      <span class="sm">wish you and your family</span>
      <span class="md">all the best for the</span>
      <span class="lg">Festive Season</span>
      <span class="lg"><span style="font-size:20px">and</span> New Year</span>
    </p>
    <p class="farewell script">We look forward to seeing you back at Marou Cay Lodge again!</p>
  </section>

</main>
</body>
</html>
```